A.I. technology startup needs a website design

We need a website design for our artificial intelligence product tqMarlo.
tqMarlo is a platform that uses the latest advances in natural language processing and machine learning to intelligently communicate to users and provide users an interface to interact with organizations through natural language. It is designed as a contact centre robot that automates the handling of customer service inquiries, thus helping to improve service quality and reduce operational expenses. Unlike any other artificial intelligence, this system is trained by using a knowledgebase combined with on-the-job training to quickly learn answers to frequently asked questions and be able to provide intelligent responses to user inquiries.
We would like this product website to show prospective customers what tqMarlo is about and to generate excitement for this product, as we are in the middle of launching out worldwide.
----------------------------------------------
The website design should be modern and clean. Our product uses cutting edge technology and we want the website to deliver this message.
We like modern style websites with large fonts and images and dynamic design.
There should be a menu at the top with the following options which will navigate the user to the appropriate page:
- tqMarlo (this acts as the home page)
- Benefits
- How It Works
- About Us
The website should be responsive for mobile device users.
Here are some examples of website designs we like:
http://www.brivelo.com/
https://www.quandersyn.com
https://www.folvaret.com/customer-support-software
https://www.parnook.com/
We have some attachments which may help in the website. Please take a look at our existing material, which includes: tqMarlo logo, tqMarlo powerpoint presentation (contains alot of content we can re-use on the website), and more.
Appreciate your creative talent and website expertise, and we look forward to seeing your designs!
Tech
Coded - Design and coding required
4 page

```html
<!DOCTYPE html>
<html lang="en">
<head>
<meta charset="utf-8">
<title>tqMarlo – Live Web Chat</title>
<link href="https://fonts.googleapis.com/css2?family=Questrial&family=Montserrat:wght@700&family=Open+Sans:wght@400;600;700&display=swap" rel="stylesheet">
<style>
:root{
  --blue:#0b6fc6;
  --blue-dark:#0a5aa3;
  --cyan:#1ab0e8;
  --ink:#1d1d1d;
  --text:#6a6a6a;
  --muted:#8a8a8a;
  --line:#e3e3e3;
  --light:#f4f5f6;
  --footer:#121416;
  --white:#ffffff;
}
*{box-sizing:border-box;margin:0;padding:0}
html,body{width:1200px;height:3543px;overflow:hidden}
body{position:relative;background:var(--white);font-family:"Open Sans",Arial,sans-serif;color:var(--text)}
.abs{position:absolute}
h2.section-title{position:absolute;left:0;width:1200px;text-align:center;font-family:"Questrial",Arial,sans-serif;font-weight:400;font-size:27px;line-height:37px;color:var(--ink)}
.section-intro{position:absolute;left:240px;width:720px;text-align:center;font-size:11.5px;line-height:22px;color:var(--text)}

/* header */
.site-header{position:absolute;left:0;top:0;width:1200px;height:104px;border-bottom:3px solid var(--blue);background:var(--white)}
.brand{position:absolute;display:flex;align-items:center;gap:10px;font-family:"Questrial",Arial,sans-serif;font-size:34px}
.brand .dot{width:34px;height:34px;border-radius:50%;background:var(--blue)}
.site-header .brand{left:132px;top:32px;color:var(--blue)}
.main-nav{position:absolute;left:505px;top:46px;display:flex;gap:0;font-family:"Questrial",Arial,sans-serif;font-size:15px;color:var(--ink)}
.main-nav a{color:inherit;text-decoration:none;margin-right:62px;display:flex;align-items:center;gap:8px}
.main-nav a.active{color:var(--cyan)}
.main-nav a.active::before{content:"";width:16px;height:16px;border-radius:50%;border:2px solid var(--cyan)}

/* hero */
.hero{position:absolute;left:0;top:104px;width:1200px;height:522px;background:linear-gradient(90deg,#f6f7f8 0%,#eef1f3 45%,#dfe5ea 100%)}
.hero-photo{position:absolute;left:470px;top:0;width:730px;height:522px;background:radial-gradient(ellipse at 40% 65%,#9cd0ee 0%,rgba(156,208,238,0) 30%),linear-gradient(90deg,rgba(235,239,242,0) 0%,#d7dde2 40%,#c9cfd5 100%)}
.hero h1{position:absolute;left:132px;top:132px;font-family:"Montserrat",Arial,sans-serif;font-size:44px;letter-spacing:1px;color:var(--ink)}
.hero p{position:absolute;left:132px;top:200px;width:480px;font-size:15px;line-height:31px;color:#3a3a3a}
.hero p span{color:var(--cyan)}
.btn{position:absolute;display:flex;align-items:center;justify-content:center;background:var(--cyan);color:var(--white);border-radius:20px;font-weight:700;font-size:12px}
.hero .btn{left:132px;top:314px;width:118px;height:38px}
.hero-dots{position:absolute;left:132px;top:434px;display:flex;gap:22px}
.hero-dots i{width:12px;height:12px;border-radius:50%;background:#a0a0a0}
.hero-dots i.on{background:var(--blue)}

/* battleground */
.monitor-shot{position:absolute;left:132px;top:862px;width:322px;height:332px}
.benefit{position:absolute;left:530px;width:530px}
.benefit .icon{position:absolute;left:0;top:0;width:62px;height:62px}
.benefit h3{position:absolute;left:86px;top:0;font-weight:400;font-size:14px;color:var(--blue-dark)}
.benefit p{position:absolute;left:86px;top:24px;width:440px;font-size:11.5px;line-height:23px;color:var(--text)}

/* features */
.features{position:absolute;left:0;top:1268px;width:1200px;height:480px;background:var(--blue)}
.features h2.section-title{top:62px;color:var(--white)}
.features .section-intro{top:98px;color:#dfeefb}
.features .section-intro span{color:#8fe3ff}
.feature-card{position:absolute;top:161px;width:300px;height:255px;background:var(--white)}
.feature-card .shot{width:100%;height:191px}
.feature-card h3{text-align:center;margin-top:14px;font-weight:400;font-size:13px;color:var(--ink)}
.feature-card p{text-align:center;font-size:11.5px;margin-top:4px;color:#444}

/* potential */
.bullet{position:absolute;left:132px;width:480px}
.bullet .icon{position:absolute;left:0;top:0;width:30px;height:30px}
.bullet p{position:absolute;left:46px;top:-3px;width:430px;font-size:11.5px;line-height:23px}
.potential .btn{left:132px;top:2263px;width:228px;height:38px}
.monitor-app{position:absolute;left:685px;top:1984px;width:384px;height:326px}

/* industries */
.industries{position:absolute;left:0;top:2378px;width:1200px;height:702px;background:var(--light);border-top:1px solid var(--line)}
.industry{position:absolute;width:270px;text-align:center}
.industry svg{display:block;margin:0 auto}
.industry h3{font-family:"Questrial",Arial,sans-serif;font-weight:400;font-size:16px;color:#2a2a2a;margin-top:6px}
.industry p{font-size:11.5px;line-height:21px;margin-top:6px}

/* footer */
.site-footer{position:absolute;left:0;top:3080px;width:1200px;height:409px;background:linear-gradient(180deg,#1b1e21,var(--footer))}
.site-footer .brand{left:132px;top:50px;color:var(--white)}
.site-footer .brand .dot{background:var(--white)}
.social{position:absolute;left:916px;top:midpoint;top:60px;display:flex;gap:5px}
.social i{width:26px;height:26px;border-radius:50%;border:1.5px solid #cfcfcf}
.footer-col h4{position:absolute;font-family:"Questrial",Arial,sans-serif;font-weight:400;font-size:16px;color:var(--white)}
.quick-links{position:absolute;left:132px;top:203px;list-style:none;font-size:12px;line-height:24px;color:#d8d8d8}
.contact-line{position:absolute;left:328px;display:flex;gap:12px;font-size:12.5px;line-height:22px;color:#e2e2e2}
.contact-line svg{flex:none;margin-top:4px}
.field{position:absolute;border:1px solid #9aa0a6;border-radius:3px;font-size:11px;color:#e0e0e0;padding:6px 10px}
.site-footer .btn{left:633px;top:321px;width:124px;height:36px}
.copyright{position:absolute;left:0;top:3489px;width:1200px;height:54px;line-height:54px;text-align:center;font-size:11px;color:#777;background:var(--white)}
</style>
</head>
<body>

<header class="site-header">
  <div class="brand"><span class="dot"></span>tqMarlo</div>
  <nav class="main-nav">
    <a class="active" href="#">Home</a>
    <a href="#">Benefits</a>
    <a href="#">How It Works</a>
    <a href="#">About Us</a>
    <a href="#">Contact us</a>
  </nav>
</header>

<section class="hero">
  <div class="hero-photo" role="img" aria-label="Photo of a woman typing on a laptop with glowing chat icons rising from the screen"></div>
  <h1>LIVE WEB CHAT</h1>
  <p><span>tqMarlo</span> tqMarlo is a platform that uses the latest advances in natural language processing and machine learning to intelligently communicate to users...</p>
  <a class="btn">Learn More Info</a>
  <div class="hero-dots"><i class="on"></i><i></i><i></i></div>
</section>

<section class="battleground">
  <h2 class="section-title" style="top:684px">Digital Customer Experience is the<br>New Battleground</h2>
  <p class="section-intro" style="top:764px">Lorem ipsum dolor sit amet, consectetur adipiscing elit, sed do eiusmod tempor incididunt ut labore et dolore magna aliqua. Ut enim ad minim veniam, quis nostrud exercitation ullamco laboris nisi ut aliquip ex ea commodo consequat. Duis aute irure dolor in reprehenderit in voluptate velit esse cillum dolore eu fugiat nulla pariatur. Excepteur sint occaecat cupidatat non proident, sunt in culpa qui officia...</p>

  <svg class="monitor-shot" viewBox="0 0 322 332" aria-label="Desktop monitor showing a rising line chart">
    <polygon points="10,0 305,48 305,300 10,272" fill="#1a1a1a"/>
    <polygon points="24,18 292,60 292,285 24,258" fill="#fafafa"/>
    <path d="M40 210 C120 205 200 190 250 110" fill="none" stroke="#1b7fd0" stroke-width="4"/>
    <path d="M40 214 C130 212 210 205 265 150" fill="none" stroke="#8aa3b8" stroke-width="3"/>
    <line x1="40" y1="222" x2="280" y2="240" stroke="#999" stroke-width="1"/>
    <text x="55" y="240" font-size="12" fill="#555">80s</text>
    <text x="110" y="245" font-size="12" fill="#555">90s</text>
    <text x="160" y="250" font-size="12" fill="#555">00s</text>
    <text x="165" y="265" font-size="12" fill="#555">Year</text>
    <text x="215" y="255" font-size="12" fill="#555">10s</text>
    <text x="262" y="259" font-size="12" fill="#555">20s</text>
    <polygon points="150,285 200,292 205,320 140,318" fill="#cfcfcf"/>
    <ellipse cx="175" cy="322" rx="70" ry="8" fill="#bdbdbd"/>
  </svg>

  <div class="benefit" style="top:870px">
    <svg class="icon" viewBox="0 0 62 62"><circle cx="31" cy="31" r="28" fill="none" stroke="var(--blue)" stroke-width="3"/><circle cx="31" cy="31" r="15" fill="none" stroke="var(--blue)" stroke-width="3"/><circle cx="31" cy="31" r="5" fill="var(--blue)"/><path d="M31 8v10M31 44v10M8 31h10M44 31h10" stroke="var(--blue)" stroke-width="3"/></svg>
    <h3>On-Demand</h3>
    <p>Lorem Ipsum is simply dummy text of the printing and typesetting industry. Lorem Ipsum has been the occaecat cupidatat industry's...</p>
  </div>
  <div class="benefit" style="top:960px">
    <svg class="icon" viewBox="0 0 62 62"><circle cx="31" cy="31" r="28" fill="none" stroke="var(--blue)" stroke-width="3"/><rect x="27" y="13" width="8" height="26" rx="4" fill="none" stroke="var(--blue)" stroke-width="3"/><circle cx="31" cy="43" r="6" fill="var(--blue)"/></svg>
    <h3>Low Friction</h3>
    <p>Lorem Ipsum is simply dummy text of the printing and typesetting industry. Lorem Ipsum has been the occaecat cupidatat industry's...</p>
  </div>
  <div class="benefit" style="top:1050px">
    <svg class="icon" viewBox="0 0 62 62"><circle cx="31" cy="31" r="28" fill="none" stroke="var(--blue)" stroke-width="3"/><path d="M44 16 C34 16 26 24 22 34 L28 40 C38 36 46 28 46 18Z" fill="var(--blue)"/><path d="M22 40 L16 46" stroke="var(--blue)" stroke-width="3"/></svg>
    <h3>Intuitive</h3>
    <p>Lorem Ipsum is simply dummy text of the printing and typesetting industry. Lorem Ipsum has been the occaecat cupidatat industry's...</p>
  </div>
</section>

<section class="features">
  <h2 class="section-title">Our Features</h2>
  <p class="section-intro"><span>Exercitation</span> ullamco laboris nisi ut aliquip ex ea commodo consequat. Duis aute irure dolor in reprehenderit in voluptate velit esse cillum dolore eu fugiat nulla pariatur. Excepteur sint occaecat cupidatat non proident, sunt in culpa qui officia...</p>
  <div class="feature-card" style="left:132px">
    <div class="shot" role="img" aria-label="Photo of a team working together at a computer" style="background:linear-gradient(135deg,#c9c2b6,#6b6a66)"></div>
    <h3>Web</h3><p>Chat with visitors on your website</p>
  </div>
  <div class="feature-card" style="left:451px">
    <div class="shot" role="img" aria-label="Photo of a hand holding a smartphone in front of a laptop" style="background:linear-gradient(135deg,#ededed,#9d9d9d)"></div>
    <h3>Mobile</h3><p>Talk to your customers on-the- go</p>
  </div>
  <div class="feature-card" style="left:768px">
    <div class="shot" role="img" aria-label="Photo of a hand touching a glowing digital interface" style="background:linear-gradient(135deg,#3e6f98,#0d2440)"></div>
    <h3>In-app</h3><p>Help users as they are using your apps</p>
  </div>
</section>

<section class="potential">
  <h2 class="section-title" style="top:1820px">Potential Customers are Already<br>On your Website</h2>
  <p class="section-intro" style="top:1902px">Lorem ipsum dolor sit amet, consectetur adipiscing elit, sed do eiusmod tempor incididunt ut labore et dolore magna aliqua. Ut enim ad minim veniam, quis nostrud exercitation ullamco laboris nisi ut aliquip ex ea commodo consequat. Duis aute irure dolor in reprehenderit...</p>

  <div class="bullet" style="top:1998px"><svg class="icon" viewBox="0 0 30 30"><circle cx="15" cy="15" r="13" fill="none" stroke="var(--cyan)" stroke-width="2"/><path d="M9 15l4 4 8-8" fill="none" stroke="var(--cyan)" stroke-width="2"/></svg><p>Aliquip ex ea commodo consequat. Duis aute irure dolor in reprehenderit in voluptate velit esse cillum dolore eu fugiat nulla pariatur. Excepteur sint...</p></div>
  <div class="bullet" style="top:2061px"><svg class="icon" viewBox="0 0 30 30"><circle cx="15" cy="15" r="13" fill="none" stroke="var(--cyan)" stroke-width="2"/><path d="M9 15l4 4 8-8" fill="none" stroke="var(--cyan)" stroke-width="2"/></svg><p>Aliquip ex ea commodo consequat. Duis aute irure dolor in reprehenderit in voluptate velit esse cillum dolore eu fugiat nulla pariatur. Excepteur sint...</p></div>
  <div class="bullet" style="top:2124px"><svg class="icon" viewBox="0 0 30 30"><circle cx="15" cy="15" r="13" fill="none" stroke="var(--cyan)" stroke-width="2"/><path d="M9 15l4 4 8-8" fill="none" stroke="var(--cyan)" stroke-width="2"/></svg><p>Aliquip ex ea commodo consequat. Duis aute irure dolor in reprehenderit in voluptate velit esse cillum dolore eu fugiat nulla pariatur. Excepteur sint...</p></div>
  <div class="bullet" style="top:2187px"><svg class="icon" viewBox="0 0 30 30"><circle cx="15" cy="15" r="13" fill="none" stroke="var(--cyan)" stroke-width="2"/><path d="M9 15l4 4 8-8" fill="none" stroke="var(--cyan)" stroke-width="2"/></svg><p>Aliquip ex ea commodo consequat. Duis aute irure dolor in reprehenderit in voluptate velit esse cillum dolore eu fugiat nulla pariatur. Excepteur sint...</p></div>
  <a class="btn">Start the Conversation with tqMarlo</a>

  <svg class="monitor-app" viewBox="0 0 384 326" aria-label="Desktop monitor showing a help page with a chat window">
    <rect x="0" y="0" width="384" height="250" rx="8" fill="#1a1a1a"/>
    <rect x="12" y="12" width="360" height="224" fill="#f4f6f8" role="img" aria-label="Screenshot of a help centre page with an open chat panel"/>
    <rect x="12" y="12" width="360" height="14" fill="#dde3ea"/>
    <rect x="140" y="36" width="120" height="92" fill="#ffffff" stroke="#4a8b4a"/>
    <rect x="240" y="210" width="22" height="10" fill="#1b63b5"/>
    <polygon points="165,250 220,250 226,300 158,300" fill="#cfcfcf"/>
    <ellipse cx="192" cy="304" rx="80" ry="8" fill="#bdbdbd"/>
  </svg>
</section>

<section class="industries">
  <h2 class="section-title" style="top:62px">Popular Industry Applications</h2>

  <div class="industry" style="left:120px;top:207px">
    <svg width="136" height="136" viewBox="0 0 136 136"><circle cx="68" cy="68" r="66" fill="#dfe3e7"/><circle cx="68" cy="68" r="58" fill="var(--blue)"/><circle cx="68" cy="68" r="34" fill="none" stroke="#fff" stroke-width="5"/><path d="M50 52c10 4 14 14 8 22M82 46c-6 10 2 18 10 20M70 94c0-8 8-12 12-6" fill="none" stroke="#fff" stroke-width="6"/></svg>
    <h3>Telecommunications</h3>
    <p>Lorem ipsum dolor sit amet, consectetur adipiscing elit, sed do eiusmod tempor incididunt ut labore et prodent dolore magna...</p>
  </div>
  <div class="industry" style="left:465px;top:143px">
    <svg width="136" height="136" viewBox="0 0 136 136"><circle cx="68" cy="68" r="66" fill="#dfe3e7"/><circle cx="68" cy="68" r="58" fill="var(--blue)"/><circle cx="68" cy="68" r="30" fill="none" stroke="#fff" stroke-width="5"/><text x="68" y="82" text-anchor="middle" font-family="Open Sans,sans-serif" font-weight="700" font-size="38" fill="#fff">$</text></svg>
    <h3>Finance &amp; Banking</h3>
    <p>Lorem ipsum dolor sit amet, consectetur adipiscing elit, sed do eiusmod tempor incididunt ut labore et prodent dolore magna...</p>
  </div>
  <div class="industry" style="left:807px;top:207px">
    <svg width="136" height="136" viewBox="0 0 136 136"><circle cx="68" cy="68" r="66" fill="#dfe3e7"/><circle cx="68" cy="68" r="58" fill="var(--blue)"/><path d="M44 58h48M48 58a20 18 0 0 1 40 0" fill="#fff" stroke="#fff" stroke-width="3"/><path d="M50 64v24M60 64v24M70 64v24M80 64v24M88 64v24" stroke="#fff" stroke-width="5"/><rect x="40" y="90" width="56" height="6" fill="#fff"/><rect x="66" y="30" width="4" height="12" fill="#fff"/></svg>
    <h3>Government</h3>
    <p>Lorem ipsum dolor sit amet, consectetur adipiscing elit, sed do eiusmod tempor incididunt ut labore et prodent dolore magna...</p>
  </div>
  <div class="industry" style="left:318px;top:408px">
    <svg width="136" height="136" viewBox="0 0 136 136"><circle cx="68" cy="68" r="66" fill="#dfe3e7"/><circle cx="68" cy="68" r="58" fill="var(--blue)"/><path d="M36 74l20-4 24-22c6-6 14-6 12 2l-22 24-4 20-6 2-2-16-16 2z" fill="#fff"/></svg>
    <h3>Transportation &amp; Travel</h3>
    <p>Lorem ipsum dolor sit amet, consectetur adipiscing elit, sed do eiusmod tempor incididunt ut labore et prodent dolore magna...</p>
  </div>
  <div class="industry" style="left:609px;top:408px">
    <svg width="136" height="136" viewBox="0 0 136 136"><circle cx="68" cy="68" r="66" fill="#dfe3e7"/><circle cx="68" cy="68" r="58" fill="var(--blue)"/><path d="M68 98 C40 78 34 64 40 52c6-12 22-12 28 0 6-12 22-12 28 0 6 12 0 26-28 46z" fill="#fff"/><path d="M68 56v26M55 69h26" stroke="var(--blue)" stroke-width="7"/></svg>
    <h3>Health &amp; Pharmaceutical &amp; Retail</h3>
    <p>Lorem ipsum dolor sit amet, consectetur adipiscing elit, sed do eiusmod tempor incididunt ut labore et prodent dolore magna...</p>
  </div>
</section>

<footer class="site-footer">
  <div class="brand"><span class="dot"></span>tqMarlo</div>
  <div class="social"><i></i><i></i><i></i><i></i><i></i></div>

  <div class="footer-col">
    <h4 style="left:132px;top:160px">Quick Link</h4>
    <ul class="quick-links"><li>Home</li><li>Benefits</li><li>How It Works</li><li>About Us</li><li>Contact us</li></ul>
  </div>
  <div class="footer-col">
    <h4 style="left:328px;top:160px">Our Location</h4>
    <div class="contact-line" style="top:196px"><svg width="12" height="16" viewBox="0 0 12 16"><path d="M6 0a6 6 0 0 1 6 6c0 4-6 10-6 10S0 10 0 6a6 6 0 0 1 6-6z" fill="#fff"/><circle cx="6" cy="6" r="2" fill="#222"/></svg><span>P.O Box 4127 Harlow Court<br>Street name City -52810</span></div>
    <div class="contact-line" style="top:260px"><svg width="12" height="14" viewBox="0 0 12 14"><path d="M2 0l3 3-2 2c1 2 3 4 5 5l2-2 3 3-2 3C5 14-1 7 2 0z" fill="#fff"/></svg><span>Help : (07) 5521 0947</span></div>
    <div class="contact-line" style="top:300px"><svg width="14" height="10" viewBox="0 0 14 10"><rect width="14" height="10" fill="#fff"/><path d="M0 0l7 6 7-6" fill="none" stroke="#222"/></svg><span>info@tqMarlo.com</span></div>
  </div>

  <div class="field" style="left:633px;top:162px;width:210px;height:32px">Name</div>
  <div class="field" style="left:857px;top:162px;width:211px;height:32px">Mail</div>
  <div class="field" style="left:633px;top:202px;width:210px;height:32px">Phone</div>
  <div class="field" style="left:857px;top:202px;width:211px;height:32px">Subject</div>
  <div class="field" style="left:633px;top:242px;width:435px;height:62px">Message</div>
  <a class="btn">SEND MESSAGE</a>
</footer>

<div class="copyright">Copyrights © tqMarlo , 2017 | All rights reserved.</div>

</body>
</html>
```